Training Company Needs a Web Design

We are a Training company that needs a website design completed for us. "The Harbor Loft" The website will be a 'community space' specialising in 'Change and Transformation'. It will be a 'space' where individuals can come to find out 'latest news', upcoming events and courses, chat with others and find 'tools and templates'. They will need to login as a 'Member'.

The final design needs to be professional but have a 'fun and interactive' feel and appeal to our target audience who are predominantly corporate individuals.

Target Market(s)

Corporate Individuals - they may have a Change or Project background

Industry/Entity Type

Business Consultant

Number of Pages Required

3 page

Font styles to use
Sans Serif

Requirements
Must have
• Design for 'Home Page'
• A professional and corporate 'feel' but be fun and interactive.
Nice to have
• A 'sense' of how some of the other pages may be designed or laid out.

```html
<!DOCTYPE html>
<html lang="en">
<head>
<meta charset="utf-8">
<title>The Harbor Loft – Change and Transformation</title>
<link href="https://fonts.googleapis.com/css2?family=Montserrat:wght@400;500;600&family=PT+Sans:wght@400;700&display=swap" rel="stylesheet">
<style>
:root{
  --navy:#0d4a8c;
  --navy-dark:#0f3f73;
  --orange:#f05223;
  --ink:#1e1e1e;
  --text:#6b6b6b;
  --white:#ffffff;
  --footer:#0d0d0f;
  --footer-bar:#070708;
  --footer-text:#c9c9c9;
  --sky:#2a8fcb;
}
*{margin:0;padding:0;box-sizing:border-box}
html,body{width:1200px;height:2296px;overflow:hidden}
body{font-family:"PT Sans",Arial,sans-serif;color:var(--text);background:var(--white);position:relative}
.heading{font-family:"Montserrat",Arial,sans-serif;color:var(--ink);font-weight:500;text-transform:uppercase;text-align:center}
.abs{position:absolute}

/* top bar */
.topbar{top:0;left:0;width:1200px;height:49px;background:var(--navy);font-family:"Montserrat",Arial,sans-serif;font-size:11px;color:var(--white);display:flex;justify-content:flex-end;align-items:center;gap:18px;padding-right:110px;text-transform:uppercase}
.topbar span{display:flex;align-items:center;gap:5px}

/* nav */
.header{top:49px;left:0;width:1200px;height:83px;background:var(--white)}
.brand{position:absolute;left:110px;top:28px;display:flex;align-items:center;gap:10px;font-family:"Montserrat",Arial,sans-serif;font-weight:600;font-size:15px;color:var(--sky);text-transform:uppercase;letter-spacing:.5px}
.brand i{display:block;width:12px;height:12px;border-radius:50%;background:var(--sky)}
.nav{position:absolute;left:540px;top:0;height:83px;display:flex;font-family:"Montserrat",Arial,sans-serif;font-size:12px;font-weight:500;color:var(--ink);text-transform:uppercase}
.nav a{display:flex;align-items:center;height:83px;padding:0 21px;text-decoration:none;color:inherit}
.nav a.active{background:var(--orange);color:var(--white);padding:0 20px}

/* hero */
.hero{top:132px;left:0;width:1200px;height:511px;background:linear-gradient(100deg,#8fa3b3 0%,#c9c2b7 30%,#6e7a88 55%,#3b4350 80%,#2a2d33 100%)}
.hero::after{content:"";position:absolute;inset:0;background:rgba(20,30,45,.25)}
.hero-inner{position:absolute;left:0;top:0;width:1200px;height:511px;z-index:1;text-align:center}
.hero h1{position:absolute;top:270px;width:100%;font-family:"Montserrat",Arial,sans-serif;font-weight:500;font-size:42px;color:var(--white);letter-spacing:.5px}
.hero .divider{top:320px}
.hero p{position:absolute;left:230px;top:362px;width:740px;font-size:12.5px;line-height:26px;color:var(--white)}
.dots{position:absolute;top:466px;left:0;width:100%;display:flex;justify-content:center;gap:10px}
.dots i{width:13px;height:13px;border-radius:50%;border:2px solid var(--white)}
.dots i.on{background:var(--orange)}

.divider{position:absolute;left:0;width:100%;display:flex;justify-content:center}

/* welcome */
.welcome-title{top:696px;left:0;width:1200px;font-size:26px}
.welcome .divider{top:738px}
.welcome-text{top:764px;left:130px;width:940px;text-align:center;font-size:12.5px;line-height:24px}
.features{top:852px;left:98px;width:1004px;display:flex;justify-content:space-between}
.feature{width:250px;text-align:center}
.feature .icon{width:80px;height:80px;border:2px solid var(--ink);border-radius:50%;margin:0 auto;display:flex;align-items:center;justify-content:center}
.feature h3{margin-top:16px;font-family:"Montserrat",Arial,sans-serif;font-weight:500;font-size:17px;color:var(--ink)}
.feature p{margin:10px auto 0;width:200px;font-size:12px;line-height:25px;text-align:justify;text-align-last:center}

/* events */
.events{top:1099px;left:0;width:1200px;height:471px;background:linear-gradient(180deg,#2a8fcb 0%,#2c86c1 45%,#1f6fa8 100%)}
.events-title{top:1160px;left:0;width:1200px;font-size:25px;color:var(--white)}
.events .divider{top:1204px}
.cards{top:1275px;left:112px;width:976px;display:flex;justify-content:space-between}
.card{width:225px;height:229px;background:var(--white);position:relative;text-align:center;box-shadow:0 4px 10px rgba(0,0,0,.15)}
.card .thumb{position:absolute;left:14px;top:-17px;width:198px;height:122px}
.card h4{position:absolute;top:129px;width:100%;font-weight:400;font-size:16px;color:#444}
.card p{position:absolute;top:160px;left:20px;width:185px;font-size:11.5px;line-height:23px;text-align:justify;text-align-last:center}

/* cta */
.cta{top:1570px;left:0;width:1200px;height:120px;background:var(--orange)}
.cta p{position:absolute;left:110px;top:32px;width:620px;font-size:15.5px;line-height:31px;color:var(--white)}
.cta .button{position:absolute;left:785px;top:34px;width:303px;height:56px;background:var(--navy-dark);border-radius:3px;display:flex;align-items:center;justify-content:center;font-family:"Montserrat",Arial,sans-serif;font-weight:500;font-size:15px;color:var(--white);text-transform:uppercase}

/* news */
.news-title{top:1730px;left:0;width:1200px;font-size:26px}
.news .divider{top:1772px}
.news-list{top:1819px;left:112px;width:976px;display:flex;justify-content:space-between}
.news-item{width:478px;display:flex;gap:15px}
.news-item .thumb{position:relative;width:179px;height:129px;flex:none}
.news-item .date{position:absolute;right:0;bottom:0;width:95px;height:36px;background:var(--navy);color:var(--white);font-size:13px;display:flex;align-items:center;justify-content:center}
.news-item h5{font-size:14.5px;font-weight:400;color:var(--ink);line-height:23px;margin-top:-4px}
.news-item p{font-size:11.5px;line-height:24px;margin-top:4px;text-align:justify}

/* footer */
.footer{top:1996px;left:0;width:1200px;height:220px;background:var(--footer);color:var(--footer-text)}
.footer h6{font-family:"Montserrat",Arial,sans-serif;font-weight:500;font-size:17px;color:var(--white);text-transform:uppercase;margin-bottom:14px}
.f-about{left:112px;top:30px;width:470px}
.f-about p{font-size:11.5px;line-height:25.5px}
.f-contact{left:646px;top:30px;width:220px;font-size:11.5px}
.f-contact .row{display:flex;gap:12px;margin-bottom:14px;line-height:20px}
.f-contact strong{color:var(--white);font-weight:700}
.f-links{left:920px;top:30px}
.f-links ul{list-style:none;font-size:11.5px;line-height:26px}
.vline{top:2026px;width:1px;height:170px;background:#26262a}
.bottombar{top:2216px;left:0;width:1200px;height:80px;background:var(--footer-bar);font-size:11.5px;color:var(--footer-text)}
.bottombar .copy{position:absolute;left:110px;top:31px}
.bottombar .copy a{color:var(--orange);text-decoration:none;margin-left:10px}
.social{position:absolute;left:990px;top:29px;display:flex;gap:5px}
.social i{width:21px;height:21px;border-radius:50%}
</style>
</head>
<body>

<div class="abs topbar">
  <span><svg width="9" height="10" viewBox="0 0 9 10"><circle cx="4.5" cy="2.6" r="2.4" fill="#fff"/><path d="M0 10c0-3 2-4.5 4.5-4.5S9 7 9 10z" fill="#fff"/></svg>Register</span>
  <span><svg width="9" height="10" viewBox="0 0 9 10"><rect x="0.5" y="4.5" width="8" height="5.5" fill="#fff"/><path d="M2 4.5V3a2.5 2.5 0 0 1 5 0v1.5" stroke="#fff" stroke-width="1.4" fill="none"/></svg>Member Login</span>
</div>

<header class="abs header">
  <div class="brand"><i></i>The Harbor Loft</div>
  <nav class="nav">
    <a class="active" href="#">Home</a>
    <a href="#">About</a>
    <a href="#">Services</a>
    <a href="#">News &amp; Events</a>
    <a href="#">Blog</a>
    <a href="#">Contact Us</a>
  </nav>
</header>

<section class="abs hero" role="img" aria-label="Business professionals in a meeting around a table">
  <div class="hero-inner">
    <h1>CHANGE AND TRANSFORMATION</h1>
    <div class="divider"><svg width="250" height="20" viewBox="0 0 250 20"><line x1="0" y1="12" x2="110" y2="12" stroke="#f05223" stroke-width="2"/><circle cx="125" cy="10" r="8" fill="none" stroke="#f05223" stroke-width="2.5"/><line x1="140" y1="12" x2="250" y2="12" stroke="#f05223" stroke-width="2"/></svg></div>
    <p>Lorem ipsum dolor sit amet, consectetur adipiscing elit. Suspendisse non finibus diam. Phasellus purus eros, mollis sit amet ipsum at, faucibus gravida orci. Ut condimentum elit massa, non tristique enim malesuada vitae. Aliquam sed viverra orci.</p>
    <div class="dots"><i></i><i class="on"></i><i></i></div>
  </div>
</section>

<section class="welcome">
  <h2 class="abs heading welcome-title">Welcome to The Harbor Loft</h2>
  <div class="divider"><svg width="120" height="16" viewBox="0 0 120 16"><line x1="0" y1="10" x2="50" y2="10" stroke="#f05223" stroke-width="2"/><circle cx="60" cy="8" r="6" fill="none" stroke="#f05223" stroke-width="2"/><line x1="70" y1="10" x2="120" y2="10" stroke="#f05223" stroke-width="2"/></svg></div>
  <p class="abs welcome-text">Lorem ipsum dolor sit amet, consectetur adipiscing elit. Suspendisse non finibus diam. Phasellus purus eros, mollis sit amet ipsum at, faucibus gravida orci. Ut condimentum elit massa, non tristique enim malesuada vitae. Aliquam sed viverra orci.</p>
  <div class="abs features">
    <div class="feature">
      <div class="icon"><svg width="30" height="30" viewBox="0 0 30 30"><circle cx="15" cy="15" r="13" fill="#1e1e1e"/><text x="15" y="21" text-anchor="middle" font-family="Montserrat, sans-serif" font-weight="600" font-size="17" fill="#fff">?</text></svg></div>
      <h3>LEARN</h3>
      <p>Sed rutrum dui vitae arcu mollis, in efficitur lorem eleifend. Mauris interdum efficitur pretium.</p>
    </div>
    <div class="feature">
      <div class="icon"><svg width="34" height="34" viewBox="0 0 34 34" fill="none" stroke="#1e1e1e" stroke-width="1.3"><polygon points="17,2 30,9.5 30,24.5 17,32 4,24.5 4,9.5"/><polygon points="17,9 24,13 24,21 17,25 10,21 10,13"/><line x1="17" y1="2" x2="17" y2="9"/><line x1="30" y1="9.5" x2="24" y2="13"/><line x1="30" y1="24.5" x2="24" y2="21"/><line x1="17" y1="32" x2="17" y2="25"/><line x1="4" y1="24.5" x2="10" y2="21"/><line x1="4" y1="9.5" x2="10" y2="13"/></svg></div>
      <h3>CONNECT</h3>
      <p>Lorem ipsum dolor sit amet, consectetur adipiscing elit. Aliquam ut finibus ex, quis iaculis nibh.</p>
    </div>
    <div class="feature">
      <div class="icon"><svg width="36" height="32" viewBox="0 0 36 32" fill="#1e1e1e" stroke="#fff" stroke-width="1.2"><rect x="11" y="2" width="14" height="13"/><rect x="3" y="16" width="14" height="13"/><rect x="19" y="16" width="14" height="13"/></svg></div>
      <h3>COLLABORATE</h3>
      <p>Mauris fringilla eget mi sit amet imperdiet. Nullam dapibus arcu in metus semper, sit amet lobortis.</p>
    </div>
    <div class="feature">
      <div class="icon"><svg width="30" height="30" viewBox="0 0 30 30"><circle cx="15" cy="15" r="13" fill="#1e1e1e"/><circle cx="19" cy="9" r="2.4" fill="#fff"/><circle cx="10" cy="15" r="2.4" fill="#fff"/><circle cx="19" cy="21" r="2.4" fill="#fff"/><path d="M19 9L10 15L19 21" stroke="#fff" stroke-width="1.4" fill="none"/></svg></div>
      <h3>SHARE</h3>
      <p>Lorem ipsum dolor sit amet, consectetur adipiscing elit. Aliquam ut finibus ex, quis iaculis nibh.</p>
    </div>
  </div>
</section>

<section class="abs events" role="img" aria-label="Blue-tinted city skyline background"></section>
<h2 class="abs heading events-title">Upcoming Events and Courses</h2>
<div class="divider events" style="position:absolute;top:1204px;height:16px;background:none"><svg width="120" height="16" viewBox="0 0 120 16"><line x1="0" y1="10" x2="50" y2="10" stroke="#fff" stroke-width="2"/><circle cx="60" cy="8" r="6" fill="none" stroke="#fff" stroke-width="2"/><line x1="70" y1="10" x2="120" y2="10" stroke="#fff" stroke-width="2"/></svg></div>
<div class="abs cards">
  <article class="card">
    <div class="thumb" role="img" aria-label="Colleagues talking in an office" style="background:linear-gradient(135deg,#9aa4ab,#5d666d)"></div>
    <h4>Vestibulum dignissim</h4>
    <p>Morbi vestibulum luctus molestie. orbi quis suscipit mauris.</p>
  </article>
  <article class="card">
    <div class="thumb" role="img" aria-label="Team shaking hands at a workshop" style="background:linear-gradient(135deg,#3c3a38,#9b8e80)"></div>
    <h4>Lorem ipsum dolor</h4>
    <p>Lorem ipsum dolor sit amet, consectetur adipiscing elit.</p>
  </article>
  <article class="card">
    <div class="thumb" role="img" aria-label="People working at computers in a bright office" style="background:linear-gradient(135deg,#e4ecf0,#8fa8b8)"></div>
    <h4>Lorem ipsum dolor</h4>
    <p>Pellentesque vehicula volutpat ligula, vitae ullamcorper ante.</p>
  </article>
  <article class="card">
    <div class="thumb" role="img" aria-label="Silhouetted team joining hands against a glowing sky" style="background:linear-gradient(135deg,#7b4d86,#f0b06a)"></div>
    <h4>Lorem ipsum dolor</h4>
    <p>Lorem ipsum dolor sit amet, consectetur adipiscing elit.</p>
  </article>
</div>

<section class="abs cta">
  <p>Lorem ipsum dolor sit amet, consectetur adipiscing elit. Vestibulum a pulvinar urna. Duis porttitor tellus sit amet purus ultricies ornare.</p>
  <div class="button">Find Tools and Templates</div>
</section>

<section class="news">
  <h2 class="abs heading news-title">Latest News</h2>
  <div class="divider" style="top:1772px"><svg width="120" height="16" viewBox="0 0 120 16"><line x1="0" y1="10" x2="50" y2="10" stroke="#f05223" stroke-width="2"/><circle cx="60" cy="8" r="6" fill="none" stroke="#f05223" stroke-width="2"/><line x1="70" y1="10" x2="120" y2="10" stroke="#f05223" stroke-width="2"/></svg></div>
  <div class="abs news-list">
    <article class="news-item">
      <div class="thumb" role="img" aria-label="Smiling colleagues gathered at a laptop" style="background:linear-gradient(135deg,#c7cbc8,#7d6a5c)"><span class="date">20 Jan 2016</span></div>
      <div>
        <h5>Ut eleifend augue dolor, nec convallis dolor feug iat eget. Donec sit amet lorem.</h5>
        <p>Vestibulum rhoncus ligula nisi, nec mollis ex hendrerit ut. Proin tellus mauris, condimentum a purus sed, conse ctetur congue est. Proin sollicitudin...</p>
      </div>
    </article>
    <article class="news-item">
      <div class="thumb" role="img" aria-label="Person facing a large question mark on a grey wall" style="background:linear-gradient(135deg,#9a9a9a,#3d3d3d)"><span class="date">18 Jan 2016</span></div>
      <div>
        <h5>Proin sollicitudin condimentum mattis. Integ er at eros laoreet, gravida ante nec,</h5>
        <p>Aenean lacus arcu, interdum non elementum sed, porttitor in purus. Sed quis nibh a lacus cursus pellentesque. Vivamus eget quam ac lectus...</p>
      </div>
    </article>
  </div>
</section>

<footer class="abs footer"></footer>
<div class="abs vline" style="left:620px"></div>
<div class="abs vline" style="left:884px"></div>
<div class="abs f-about" style="top:2026px">
  <h6>About Us</h6>
  <p>Ut condimentum elit massa, non tristique enim malesuada vitae. Aliquam sed viverra orci. Etiam in mattis est. Pellentesque a condimentum ante, at elementum metus. Nullam auctor, libero in auctor mollis, orci justo hendrerit mi, sit amet tempor ligula metus et lacus. Nulla facilisis cursus commodo. Nam facilisis turpis ut odio faucibus, in condimentum eros eleifend. Sed ac tincidunt justo. Maecenas nunc enim, interdum.</p>
</div>
<div class="abs f-contact" style="top:2026px">
  <h6>Contact Us</h6>
  <div class="row"><svg width="10" height="14" viewBox="0 0 10 14"><path d="M5 0a5 5 0 0 1 5 5c0 3.5-5 9-5 9S0 8.5 0 5a5 5 0 0 1 5-5z" fill="#f05223"/><circle cx="5" cy="5" r="1.8" fill="#0d0d0f"/></svg><div><strong>THE HARBOR LOFT</strong><br>123, Lorem Ipsm, Lorem Ipsm<br>Lorem ipsm - 123 456</div></div>
  <div class="row"><svg width="14" height="11" viewBox="0 0 14 11"><rect width="14" height="11" rx="1" fill="#f05223"/><path d="M1 1.5L7 6l6-4.5" stroke="#0d0d0f" stroke-width="1.3" fill="none"/></svg><span>info@domainname.com</span></div>
  <div class="row"><svg width="14" height="14" viewBox="0 0 14 14"><rect width="14" height="14" rx="2" fill="#f05223"/><path d="M4 3.5c.5 3 2.5 6 6.5 7l1-1.5-2-1-1 .8c-1-.5-2-1.5-2.5-2.5l.8-1-1-2z" fill="#0d0d0f"/></svg><span>+123 456 789 000</span></div>
</div>
<div class="abs f-links" style="top:2026px">
  <h6>Quick Links</h6>
  <ul>
    <li>About Us</li>
    <li>Why Choose Us?</li>
    <li>Our Services</li>
    <li>Contact Us</li>
    <li>Faq</li>
  </ul>
</div>

<div class="abs bottombar">
  <div class="copy">Copyright © 2016 The Harbor Loft. All Rights Reserved. <a href="#">Privacy Policy</a><a href="#">Terms of Service</a></div>
  <div class="social"><i style="background:#3b5998"></i><i style="background:#29a9e1"></i><i style="background:#d9312b"></i><i style="background:#dc4a38"></i></div>
</div>

</body>
</html>
```